Business Card and Logo tweak for a Language Boarding School

we are a boadring langauge school for under 18 international student.
We call ourselves " TWSC" - Tarravale Worldwide Studies Centre
We are one of the RV "rosewood venture" Melbourne campus for RV high school preparation program.

our address is 19 Tolley Road Elmsbury 3920
Ph: 03 84210563
Email: info@mytwsc.com
Website: www.mytwsc.com

We have our TWSC logo, but not very satisfied. May be you can tweak it furhter with the fond or formations.

Basically the business card list all relevant info on one side and list all our programs on the other side.

The program we have:
ELICOS with Boarding for U18 Students
HSP-High School Preparation Program
PSP- Primary School Preparation Program
Junior Holiday Program & Study Tours
After School Tutoring
Student Wellbeing and Counselling

```html
<!DOCTYPE html>
<html lang="en">
<head>
<meta charset="utf-8">
<title>TWSC Business Card</title>
<link rel="stylesheet" href="https://fonts.googleapis.com/css2?family=Montserrat:wght@400;500&family=Oswald:wght@500&display=swap">
<style>
  :root {
    --backdrop: #3a3a3a;
    --card-white: #ffffff;
    --card-dark: #1f1f1f;
    --ink-dark: #222222;
    --ink-light: #ffffff;
    --cyan: #12f0ea;
    --lime: #a6e22a;
    --crimson: #f0134f;
    --amber: #ffa51c;
    --violet: #4b1fa0;
  }
  * { box-sizing: border-box; margin: 0; padding: 0; }
  html, body {
    width: 1200px; height: 1200px; overflow: hidden;
    background: var(--backdrop);
  }
  .canvas {
    position: relative; width: 1200px; height: 1200px;
    display: flex; flex-direction: column; align-items: center; justify-content: center; gap: 60px;
  }
  .card {
    position: relative; width: 880px; height: 503px;
    border-radius: 34px; overflow: hidden;
    box-shadow: 0 14px 30px rgba(0,0,0,.45);
  }
  .card-front { background: var(--card-white); }
  .card-back { background: var(--card-dark); }
  .card-split { position: absolute; inset: 0; width: 100%; height: 100%; }

  .brand {
    position: absolute; display: flex; align-items: center; gap: 26px;
    font-family: "Montserrat", sans-serif; font-weight: 500;
  }
  .brand-mark { width: 64px; height: 64px; border-radius: 50%; flex: none; }
  .brand-name { font-size: 34px; line-height: 1.05; letter-spacing: .5px; text-transform: uppercase; white-space: nowrap; }
  .card-front .brand { left: 150px; top: 62px; color: var(--ink-dark); }
  .card-front .brand-mark { background: var(--ink-dark); }
  .card-back .brand { left: 200px; top: 150px; color: var(--ink-light); }
  .card-back .brand-mark { background: var(--ink-light); }

  .programs {
    position: absolute; left: 60px; right: 60px; top: 330px;
    color: var(--ink-light); text-align: center;
  }
  .programs-title {
    font-family: "Montserrat", sans-serif; font-weight: 500;
    font-size: 19px; letter-spacing: 1px; margin-bottom: 12px;
  }
  .programs-list {
    list-style: none; display: flex; flex-wrap: wrap; justify-content: center; gap: 4px 14px;
    font-family: "Oswald", sans-serif; font-weight: 500; font-size: 17px; text-transform: uppercase;
  }
  .programs-list li { display: flex; align-items: center; gap: 7px; white-space: nowrap; }
  .dot { width: 7px; height: 7px; border-radius: 50%; display: inline-block; }

  .contacts {
    position: absolute; left: 200px; right: 60px; bottom: 78px;
    display: grid; grid-template-columns: auto auto; justify-content: space-between; gap: 16px 40px;
    font-family: "Montserrat", sans-serif; font-weight: 400; font-size: 20px; color: var(--ink-light);
  }
  .contact { display: flex; align-items: center; gap: 12px; white-space: nowrap; }
  .contact svg { width: 22px; height: 22px; flex: none; }
</style>
</head>
<body>
<main class="canvas">

  <section class="card card-front" aria-label="Programs side">
    <svg class="card-split" viewBox="0 0 880 503" preserveAspectRatio="none" aria-hidden="true">
      <polygon points="0,290 880,190 880,503 0,503" fill="var(--card-dark)"/>
      <polygon points="0,276 176,256 176,270 0,290" fill="var(--cyan)"/>
      <polygon points="176,256 334,238 334,252 176,270" fill="var(--lime)"/>
      <polygon points="334,238 616,206 616,220 334,252" fill="var(--crimson)"/>
      <polygon points="616,206 880,176 880,190 616,220" fill="var(--amber)"/>
    </svg>
    <div class="brand">
      <span class="brand-mark"></span>
      <span class="brand-name">Tarravale<br>Worldwide<br>Studies<br>Centre</span>
    </div>
    <div class="programs">
      <h2 class="programs-title">OUR PROGRAMS</h2>
      <ul class="programs-list">
        <li><span class="dot" style="background:var(--lime)"></span>ELICOS with Boarding for U18 Students</li>
        <li><span class="dot" style="background:var(--amber)"></span>HSP-High School Preparation Program</li>
        <li><span class="dot" style="background:var(--violet)"></span>PSP- Primary School Preparation Program</li>
        <li><span class="dot" style="background:var(--cyan)"></span>Junior Holiday Program &amp; Study Tours</li>
        <li><span class="dot" style="background:var(--crimson)"></span>After School Tutoring</li>
        <li><span class="dot" style="background:var(--lime)"></span>Student Wellbeing and Counselling</li>
      </ul>
    </div>
  </section>

  <section class="card card-back" aria-label="Contact side">
    <div class="brand">
      <span class="brand-mark"></span>
      <span class="brand-name">Tarravale<br>Worldwide<br>Studies<br>Centre</span>
    </div>
    <div class="contacts">
      <div class="contact">
        <svg viewBox="0 0 24 24" aria-hidden="true"><path fill="#fff" d="M6.6 10.8a15 15 0 0 0 6.6 6.6l2.2-2.2a1 1 0 0 1 1-.25 11.4 11.4 0 0 0 3.6.57 1 1 0 0 1 1 1V20a1 1 0 0 1-1 1A17 17 0 0 1 3 4a1 1 0 0 1 1-1h3.5a1 1 0 0 1 1 1c0 1.250.2 2.45.57 3.6a1 1 0 0 1-.25 1z"/></svg>
        <span>03 84210563</span>
      </div>
      <div class="contact">
        <svg viewBox="0 0 24 24" aria-hidden="true"><circle cx="12" cy="12" r="9" fill="none" stroke="#fff" stroke-width="1.8"/><ellipse cx="12" cy="12" rx="4" ry="9" fill="none" stroke="#fff" stroke-width="1.5"/><path d="M3 12h18M5 7h14M5 17h14" stroke="#fff" stroke-width="1.5"/></svg>
        <span>www.mytwsc.com</span>
      </div>
      <div class="contact">
        <svg viewBox="0 0 24 24" aria-hidden="true"><rect x="3" y="6" width="18" height="12" fill="#fff"/><path d="M3 6l9 7 9-7M3 18l7-6M21 18l-7-6" fill="none" stroke="var(--card-dark)" stroke-width="1.5"/></svg>
        <span>info@mytwsc.com</span>
      </div>
      <div class="contact">
        <svg viewBox="0 0 24 24" aria-hidden="true"><path fill="#fff" d="M12 2a7 7 0 0 0-7 7c0 5 7 13 7 13s7-8 7-13a7 7 0 0 0-7-7zm0 9.5A2.5 2.5 0 1 1 12 6.5a2.5 2.5 0 0 1 0 5z"/></svg>
        <span>19 Tolley Road Elmsbury 3920</span>
      </div>
    </div>
  </section>

</main>
</body>
</html>
```